JT Holly Cleaning Business Card

We need a business card for our new business, a cleaning company using steam. We already have a logo, and would like a modern-looking card using colors that go well with those in our logo.

```html
<!DOCTYPE html>
<html lang="en">
<head>
<meta charset="utf-8">
<title>JT Holly Cleaning – Business Card</title>
<link rel="stylesheet" href="https://fonts.googleapis.com/css2?family=Open+Sans:wght@400;700&display=swap">
<style>
  :root {
    --backdrop: #ecebe8;
    --card-white: #ffffff;
    --brand-blue: #2e6fc0;
    --wave-blue: #1f6fc6;
    --wave-sky: #3aa3e0;
    --green-light: #8cc63f;
    --green: #3fa540;
    --green-deep: #1f8f3f;
    --ink-white: #ffffff;
  }
  * { margin: 0; padding: 0; box-sizing: border-box; }
  html, body { width: 1200px; height: 1000px; overflow: hidden; }
  body {
    background: var(--backdrop);
    font-family: "Open Sans", Arial, sans-serif;
    position: relative;
  }
  .card {
    position: absolute;
    left: 265px;
    width: 667px;
    height: 397px;
    background: var(--card-white);
    overflow: hidden;
    box-shadow: 0 6px 18px rgba(0,0,0,0.18);
  }
  .card--front { top: 73px; }
  .card--back { top: 533px; }
  .card__waves { position: absolute; inset: 0; width: 100%; height: 100%; }

  .brand-name {
    position: absolute;
    color: var(--brand-blue);
    font-weight: 700;
    line-height: 1;
    white-space: nowrap;
  }
  .card--front .brand-name { left: 80px; top: 100px; font-size: 30px; }
  .card--back .brand-name { left: 0; right: 0; top: 140px; text-align: center; font-size: 42px; }

  .holder {
    position: absolute;
    right: 384px;
    top: 300px;
    text-align: right;
    color: var(--ink-white);
  }
  .holder__name { font-weight: 700; font-size: 18px; letter-spacing: 0.3px; }
  .holder__role { font-size: 16px; margin-top: 1px; }

  .divider {
    position: absolute;
    left: 315px;
    top: 280px;
    width: 2px;
    height: 90px;
    background: var(--ink-white);
  }
  .contacts {
    position: absolute;
    left: 350px;
    top: 283px;
    list-style: none;
    color: var(--ink-white);
    font-size: 15px;
    line-height: 21.5px;
  }
  .contacts li { display: flex; align-items: center; gap: 7px; }
  .contacts svg { width: 14px; height: 14px; fill: var(--ink-white); flex: none; }
</style>
</head>
<body>

<section class="card card--front" aria-label="Business card front">
  <svg class="card__waves" viewBox="0 0 667 397" preserveAspectRatio="none" aria-hidden="true">
    <defs>
      <radialGradient id="frontGreen" cx="0.45" cy="0.75" r="0.7">
        <stop offset="0" stop-color="var(--green-light)"/>
        <stop offset="0.55" stop-color="var(--green)"/>
        <stop offset="1" stop-color="var(--green-deep)"/>
      </radialGradient>
    </defs>
    <path d="M500 0 C585 55 560 248 430 250 C320 252 190 180 0 282 L0 397 L667 397 L667 0 Z" fill="var(--wave-blue)"/>
    <path d="M525 0 C600 60 570 262 432 265 C325 268 200 200 28 300 C15 310 10 340 12 397 L667 397 L667 0 Z" fill="var(--wave-sky)"/>
    <path d="M548 0 C615 70 580 272 432 274 C330 276 210 212 40 308 C30 318 25 345 26 397 L667 397 L667 0 Z" fill="url(#frontGreen)"/>
  </svg>

  <p class="brand-name">JT Holly Cleaning</p>

  <div class="holder">
    <p class="holder__name">Daniel Whitford</p>
    <p class="holder__role">Owner</p>
  </div>
  <span class="divider"></span>
  <ul class="contacts">
    <li><svg viewBox="0 0 16 16"><path d="M3 2h3l1.5 3.5-2 1.2a9 9 0 0 0 3.8 3.8l1.2-2L14 10v3a1 1 0 0 1-1 1A12 12 0 0 1 2 3a1 1 0 0 1 1-1z"/></svg>555.301.2847</li>
    <li><svg viewBox="0 0 16 16"><path d="M1 3h14v10H1z M2 4l6 5 6-5" fill="none" stroke="#fff" stroke-width="1.6"/></svg>dan@jthollycleaning.com</li>
    <li><svg viewBox="0 0 16 16"><g fill="none" stroke="#fff" stroke-width="1.4"><circle cx="8" cy="8" r="6.5"/><ellipse cx="8" cy="8" rx="3" ry="6.5"/><path d="M1.5 8h13M2.5 4.8h11M2.5 11.2h11"/></g></svg>jthollycleaning.com</li>
    <li><svg viewBox="0 0 16 16"><path d="M8 1a5 5 0 0 0-5 5c0 4 5 9 5 9s5-5 5-9a5 5 0 0 0-5-5zm0 7a2 2 0 1 1 0-4 2 2 0 0 1 0 4z"/></svg>14 Larkspur Way Eltham VIC 3095</li>
  </ul>
</section>

<section class="card card--back" aria-label="Business card back">
  <svg class="card__waves" viewBox="0 0 667 397" preserveAspectRatio="none" aria-hidden="true">
    <defs>
      <linearGradient id="backGreen" x1="0" y1="0" x2="1" y2="0">
        <stop offset="0" stop-color="var(--green-light)"/>
        <stop offset="0.5" stop-color="var(--green)"/>
        <stop offset="1" stop-color="var(--green-deep)"/>
      </linearGradient>
    </defs>
    <path d="M0 290 C120 272 260 300 400 340 C520 372 610 330 667 240 L667 397 L0 397 Z" fill="var(--wave-blue)"/>
    <path d="M0 304 C130 288 270 318 410 352 C530 380 620 345 667 262 L667 397 L0 397 Z" fill="var(--wave-sky)"/>
    <path d="M0 310 C130 296 270 326 410 360 C530 387 625 352 667 278 L667 397 L0 397 Z" fill="url(#backGreen)"/>
  </svg>

  <p class="brand-name">JT Holly Cleaning</p>
</section>

</body>
</html>
```